Price Sheet for Strength and Conditioning Facility

I need a price sheet for a training facility in Albuquerque, NM. This sheet should represent your brand and look of our facility.
Why of the Copperfield Yard?
With the help of our highly skilled team of coaches and professional educators we will help you expand your strategies to develop a new you. We will teach you how and why to balance your workouts, nutrition, recovery, sleep and mental focus to become the optimal you. We incorporate an athlete centered approach, and “yes” you are an athlete. Like the great Hal Dempsey said “If you have a body, you are an athlete.” We will help you integrate a more centered approach to your health and wellness, you will be empowered to push through until you reach your goal.
Target Market(s)
Active adults and youth athletes
Industry/Entity Type
Training
Contact Information for Business Card
Gordon Pietrowski, CSCS
Mobile number: 505-481-2267
Office: 505-372-8846
Font styles to use
Colors
Designer to choose colors to be used in the design.
Requirements
Must have
- Simple layout
- Ranch style theme
- broken into categories of services
- Use color and type font sheet
- NO TABLE! please make the table more pleasing to the eye.
Nice to have
- 8 1/2 x 11 inch sheet. Variable depending on design
- Business address: 3418 Juniper Way NE Ste. B
- Albuquerque, NM 87142
- www.thecopperfieldyard.example
- 505-372-8846

```html
<!DOCTYPE html>
<html lang="en">
<head>
<meta charset="utf-8">
<title>Copperfield Yard – Pricing Schedule</title>
<link rel="stylesheet" href="https://fonts.googleapis.com/css2?family=Didact+Gothic&family=Russo+One&family=Teko:wght@500;600&display=swap">
<style>
  :root {
    --rust: #d9472b;
    --rust-dark: #8c2a17;
    --teal: #1fa8a6;
    --cell: #f0eeed;
    --footer: #e7e5e4;
    --ink: #2b2b2b;
    --white: #ffffff;
  }
  * { box-sizing: border-box; margin: 0; padding: 0; }
  html, body { width: 927px; height: 1200px; overflow: hidden; background: var(--white); }
  body { font-family: "Didact Gothic", sans-serif; color: var(--ink); position: relative; }

  .hero {
    position: absolute; left: 0; top: 0; width: 927px; height: 232px;
    background: linear-gradient(90deg, #6e1f10 0%, #c9401f 35%, #b33a1c 60%, #7a2412 100%);
  }
  .hero-brand {
    position: absolute; left: 0; width: 927px; top: 50px;
    display: flex; justify-content: center; align-items: center; gap: 8px;
  }
  .hero-brand .dot { width: 14px; height: 14px; border-radius: 50%; background: var(--white); }
  .hero-brand span { font-family: "Teko", sans-serif; font-weight: 500; font-size: 22px; color: var(--white); letter-spacing: 2px; text-transform: uppercase; }
  .hero-title {
    position: absolute; left: 0; width: 927px; top: 146px; text-align: center;
    font-family: "Teko", sans-serif; font-weight: 600; font-size: 64px; line-height: 1;
    color: var(--white); letter-spacing: 1px; transform: scaleX(0.82);
  }

  .section { position: absolute; }
  .section-title {
    font-family: "Russo One", sans-serif; color: var(--teal); font-size: 27px;
    letter-spacing: 3px; text-align: center; line-height: 1;
  }
  .section-sub { text-align: center; font-size: 11px; margin-top: 7px; }
  .section-sub b { color: var(--rust); font-weight: 700; }

  .rates { display: grid; gap: 5px; margin-top: 20px; }
  .rates.three { grid-template-columns: repeat(3, 1fr); grid-auto-rows: 31px; }
  .rates.four { grid-template-columns: repeat(4, 1fr); grid-auto-rows: 53px; }
  .rates .head {
    background: var(--rust); color: var(--white); font-size: 14px;
    display: flex; align-items: center; justify-content: center; text-align: center; line-height: 1.15;
  }
  .rates.three .head { height: 50px; }
  .rates .cell {
    background: var(--cell); font-size: 13px;
    display: flex; align-items: center; justify-content: center;
  }
  .rates.three { grid-template-rows: 50px; }
  .rates.four { grid-template-rows: 50px; }
  sup { font-size: 7px; }
  .plan-note {
    grid-column: 1 / -1; background: var(--cell); height: 60px;
    display: flex; flex-direction: column; align-items: center; justify-content: center;
    font-size: 13.5px; line-height: 1.2; margin-top: 0;
  }

  .massage { position: absolute; left: 62px; top: 966px; width: 800px; height: 36px; }
  .massage svg { position: absolute; left: 0; top: 0; }
  .massage-label {
    position: absolute; left: 0; width: 300px; top: 0; height: 36px; line-height: 38px; text-align: center;
    font-family: "Russo One", sans-serif; color: var(--white); font-size: 20px; letter-spacing: 2px;
  }
  .massage-info { position: absolute; left: 330px; right: 0; top: 0; height: 36px; line-height: 36px; text-align: center; font-size: 13.5px; }

  .fine-print { position: absolute; left: 62px; top: 1038px; font-size: 8px; letter-spacing: 0.2px; }

  .footer { position: absolute; left: 0; top: 1074px; width: 927px; height: 126px; background: var(--footer); }
  .contact { position: absolute; left: 110px; top: 28px; width: 440px; text-align: center; }
  .contact-line { font-size: 12.5px; display: flex; justify-content: center; align-items: center; gap: 4px; }
  .contact-line .gap { width: 10px; }
  .web { margin-top: 8px; color: var(--rust); font-weight: 700; font-size: 15.5px; font-family: "Didact Gothic", sans-serif; -webkit-text-stroke: 0.4px var(--rust); }
  .footer-brand { position: absolute; left: 595px; top: 31px; display: flex; align-items: center; gap: 12px; }
  .footer-brand .ring { width: 52px; height: 52px; border-radius: 50%; border: 5px solid var(--rust); }
  .footer-brand span { font-family: "Russo One", sans-serif; font-size: 19px; letter-spacing: 2px; line-height: 1.05; color: var(--ink); text-transform: uppercase; }
</style>
</head>
<body>
  <header class="hero" role="img" aria-label="Photo of coaches working with an athlete beside a barbell rack, tinted in rust red">
    <div class="hero-brand"><div class="dot"></div><span>Copperfield Yard</span></div>
    <h1 class="hero-title">PRICING SCHEDULE</h1>
  </header>

  <section class="section" style="left:54px; top:298px; width:393px;">
    <h2 class="section-title">PRIVATE TRAINING</h2>
    <p class="section-sub"><b>1 on 1</b> Individualized time for your specific needs</p>
    <div class="rates three">
      <div class="head">Sessions/week</div><div class="head">$ per Session<sup>*</sup></div><div class="head">$ per month<sup>*</sup></div>
      <div class="cell">1</div><div class="cell">70</div><div class="cell">349</div>
      <div class="cell">2</div><div class="cell">65</div><div class="cell">679</div>
      <div class="cell">3</div><div class="cell">60</div><div class="cell">899</div>
      <div class="plan-note"><span>All plans above include one massage per month*</span><span>Includes unlimited classes per week.</span></div>
    </div>
  </section>

  <section class="section" style="left:474px; top:298px; width:393px;">
    <h2 class="section-title">PARTNER TRAINING</h2>
    <p class="section-sub"><b>2 on 1</b> Shared session with one other</p>
    <div class="rates three">
      <div class="head">Sessions/week</div><div class="head">$ per session<sup>*</sup></div><div class="head">$ per month<sup>*</sup></div>
      <div class="cell">1</div><div class="cell">70</div><div class="cell">349</div>
      <div class="cell">2</div><div class="cell">65</div><div class="cell">679</div>
      <div class="cell">3</div><div class="cell">60</div><div class="cell">899</div>
      <div class="plan-note"><span>All plans above include one massage per month*</span><span>Includes unlimited classes per week.</span></div>
    </div>
  </section>

  <section class="section" style="left:58px; top:648px; width:392px;">
    <h2 class="section-title">GROUP TRAINING</h2>
    <p class="section-sub"><b>3-5 per group</b> Individualized time for your specific needs</p>
    <div class="rates three">
      <div class="head">Sessions/week</div><div class="head">$ per session<sup>*</sup></div><div class="head">$ per month<sup>*</sup></div>
      <div class="cell">1</div><div class="cell">70</div><div class="cell">349</div>
      <div class="cell">2</div><div class="cell">65</div><div class="cell">679</div>
      <div class="cell">3</div><div class="cell">60</div><div class="cell">899</div>
      <div class="plan-note"><span>All plans above include one massage per month*</span><span>Includes unlimited classes per week.</span></div>
    </div>
  </section>

  <section class="section" style="left:478px; top:648px; width:387px;">
    <h2 class="section-title">CLASS TRAINING</h2>
    <p class="section-sub"><b>4-9 per class</b> Enhance your movement, strength and efficiency</p>
    <div class="rates four">
      <div class="head">Sessions/<br>week</div><div class="head">$ per<br>session<sup>*</sup></div><div class="head">$ per<br>month<sup>*</sup></div><div class="head">Classes/<br>week</div>
      <div class="cell">1</div><div class="cell">70</div><div class="cell">349</div><div class="cell">1</div>
      <div class="cell">2</div><div class="cell">65</div><div class="cell">679</div><div class="cell">2</div>
      <div class="cell">3</div><div class="cell">60</div><div class="cell">899</div><div class="cell">Unlimited</div>
    </div>
  </section>

  <div class="massage">
    <svg width="800" height="36" viewBox="0 0 800 36" aria-hidden="true">
      <rect x="0" y="0" width="800" height="36" fill="var(--cell)"/>
      <polygon points="0,0 322,0 290,36 0,36" fill="var(--rust)"/>
      <line x1="322" y1="0" x2="290" y2="36" stroke="var(--white)" stroke-width="3"/>
    </svg>
    <div class="massage-label">SPORTS MASSAGE</div>
    <div class="massage-info">Additional appointments available $60<sup>*</sup> per session</div>
  </div>

  <p class="fine-print"><sup>*</sup>SCHEDULES AND PRICES CURRENT 12/2017 AND SUBJECT TO CHANGE WITHOUT NOTICE.</p>

  <footer class="footer">
    <div class="contact">
      <p class="contact-line">
        <svg width="10" height="12" viewBox="0 0 10 12" aria-hidden="true"><path d="M5 0.5a4 4 0 0 1 4 4c0 3-4 7-4 7s-4-4-4-7a4 4 0 0 1 4-4z" fill="none" stroke="var(--rust)" stroke-width="1.4"/><circle cx="5" cy="4.5" r="1.4" fill="var(--rust)"/></svg>
        <span>3418 Juniper Way NE Ste. B, Albuquerque, NM 87142</span>
        <span class="gap"></span>
        <svg width="13" height="10" viewBox="0 0 13 10" aria-hidden="true"><path d="M1 3.5Q6.5-1 12 3.5L10 5 8.5 3.5h-4L3 5z" fill="var(--rust)"/><rect x="3" y="5.5" width="7" height="4" rx="1" fill="var(--rust)"/></svg>
        <span>505-372-8846</span>
      </p>
      <p class="web">www.thecopperfieldyard.example</p>
    </div>
    <div class="footer-brand">
      <div class="ring"></div>
      <span>Copperfield<br>Yard</span>
    </div>
  </footer>
</body>
</html>
```